Criação de Papelaria Profissional para Beleza
" CLÍNICA DE ESTÉTICA COMPLETA, COM ÊNFASE EM ATENDIMENTO PRÊMIUM (salas exclusivas, máquinas próprias, ambiente aconchegante com forte conexão nordestina) Serviços ofertados: Estética corporal, facial, injetáveis e laser) SITE: https://brunelva.com.br/ "

```html
<!DOCTYPE html>
<html lang="pt-BR">
<head>
<meta charset="utf-8">
<title>Brunelva – Papelaria</title>
<link rel="stylesheet" href="https://fonts.googleapis.com/css2?family=Cormorant+Garamond:wght@400;500&family=Montserrat:wght@300;400&display=swap">
<style>
  :root {
    --page: #ece7e3;
    --paper: #f6f3f0;
    --rose: #c98678;
    --rose-card: #d39a8d;
    --rose-watermark: rgba(214, 160, 148, 0.16);
    --rose-pattern: rgba(246, 222, 216, 0.28);
    --ink-light: #fbf3f0;
  }
  * { box-sizing: border-box; margin: 0; padding: 0; }
  html, body { width: 1200px; height: 1200px; overflow: hidden; }
  body {
    background: var(--page);
    display: flex;
    flex-direction: column;
    align-items: center;
    justify-content: center;
    gap: 60px;
    font-family: "Montserrat", sans-serif;
  }
  .card {
    width: 900px;
    height: 500px;
    position: relative;
    overflow: hidden;
    box-shadow: 0 10px 30px rgba(90, 60, 50, 0.15);
  }

  /* Front */
  .card-front { background: var(--paper); }
  .front-watermark {
    position: absolute;
    left: -90px;
    top: 150px;
    width: 460px;
    height: 440px;
    border-radius: 50%;
    background: radial-gradient(ellipse at center, var(--rose-watermark) 0%, var(--rose-watermark) 55%, rgba(214, 160, 148, 0) 72%);
  }
  .front-brand {
    position: absolute;
    left: 420px;
    top: 110px;
    width: 420px;
    display: flex;
    flex-direction: column;
    align-items: center;
    color: var(--rose);
  }
  .brand-dot {
    width: 92px;
    height: 92px;
    border-radius: 50%;
    background: var(--rose);
    margin-bottom: 34px;
  }
  .brand-name {
    font-family: "Cormorant Garamond", serif;
    font-weight: 400;
    font-size: 58px;
    letter-spacing: 0.32em;
    margin-right: -0.32em;
    line-height: 1;
  }
  .brand-tagline {
    font-family: "Montserrat", sans-serif;
    font-weight: 300;
    font-size: 15px;
    letter-spacing: 0.28em;
    margin-right: -0.28em;
    margin-top: 16px;
  }

  /* Back */
  .card-back { background: var(--rose-card); color: var(--ink-light); }
  .back-pattern {
    position: absolute;
    right: 0;
    top: 0;
    width: 560px;
    height: 500px;
    background:
      linear-gradient(90deg, var(--rose-card) 0%, rgba(211, 154, 141, 0) 22%),
      linear-gradient(160deg, var(--rose-pattern) 0%, rgba(246, 222, 216, 0.18) 60%, rgba(246, 222, 216, 0.1) 100%);
  }
  .back-brand {
    position: absolute;
    left: 60px;
    top: 100px;
    display: flex;
    flex-direction: column;
    align-items: center;
    width: 280px;
  }
  .back-brand .brand-dot {
    width: 44px;
    height: 44px;
    background: var(--ink-light);
    margin-bottom: 14px;
  }
  .back-brand .brand-name { font-size: 30px; }
  .back-brand .brand-tagline { font-size: 9px; margin-top: 8px; }
  .contact-list {
    position: absolute;
    left: 60px;
    top: 300px;
    list-style: none;
    display: flex;
    flex-direction: column;
    gap: 14px;
    font-size: 15px;
    font-weight: 400;
    letter-spacing: 0.03em;
  }
  .contact-item { display: flex; align-items: center; gap: 12px; }
  .contact-icon { width: 18px; height: 18px; flex: none; }
</style>
</head>
<body>

  <section class="card card-front">
    <div class="front-watermark" role="img" aria-label="Marca floral em tom rosa muito claro, como marca-d'água"></div>
    <div class="front-brand">
      <div class="brand-dot"></div>
      <div class="brand-name">BRUNELVA</div>
      <div class="brand-tagline">CLÍNICA DE ESTÉTICA</div>
    </div>
  </section>

  <section class="card card-back">
    <div class="back-pattern" role="img" aria-label="Padrão decorativo de pequenas flores claras espalhadas sobre o rosa"></div>

    <div class="back-brand">
      <div class="brand-dot"></div>
      <div class="brand-name">BRUNELVA</div>
      <div class="brand-tagline">CLÍNICA DE ESTÉTICA</div>
    </div>

    <ul class="contact-list">
      <li class="contact-item">
        <svg class="contact-icon" viewBox="0 0 24 24" fill="none" stroke="currentColor" stroke-width="1.8" stroke-linecap="round" stroke-linejoin="round"><path d="M5 3h4l2 5-2.5 1.5a11 11 0 0 0 6 6L16 13l5 2v4a2 2 0 0 1-2 2A17 17 0 0 1 3 5a2 2 0 0 1 2-2z"/></svg>
        <span>(81) 98000-0000</span>
      </li>
      <li class="contact-item">
        <svg class="contact-icon" viewBox="0 0 24 24" fill="none" stroke="currentColor" stroke-width="1.8"><circle cx="12" cy="12" r="9"/><path d="M3 12h18M12 3c3 3 3 15 0 18M12 3c-3 3-3 15 0 18"/></svg>
        <span>brunelva.com.br</span>
      </li>
      <li class="contact-item">
        <svg class="contact-icon" viewBox="0 0 24 24" fill="none" stroke="currentColor" stroke-width="1.8"><circle cx="12" cy="12" r="9"/></svg>
        <span>@brunelva.estetica</span>
      </li>
      <li class="contact-item">
        <svg class="contact-icon" viewBox="0 0 24 24" fill="none" stroke="currentColor" stroke-width="1.8" stroke-linejoin="round"><path d="M12 21s-7-7-7-12a7 7 0 0 1 14 0c0 5-7 12-7 12z"/><circle cx="12" cy="9" r="2.5"/></svg>
        <span>Rua das Flores, 120 · Recife</span>
      </li>
    </ul>
  </section>

</body>
</html>
```